Quorvex - Automated robotic Inspection with AI need new business cards

We need a new design of our business cards. The company is focused on automated quality control at high speed with unmatched results. We have a logo but need a more forward leaning business card that shows that we are delivering cutting edge technology.

Contact Information for Business Card

Name
Position
Adress
Phone
Email
e.g.
Lena Holmqvist
Chief Financial Officer (CFO)

Quorvex Sweden AB
Bruksvägen 14, SE-175 43 JÄRFÄLLA, Sweden
Mobile: +46735 21 47 83 | Office: +46 8 61 94 27
www.quorvex-example.com

Font styles to use
Sans Serif

```html
<!DOCTYPE html>
<html lang="en">
<head>
<meta charset="utf-8">
<title>Quorvex Business Cards</title>
<link rel="stylesheet" href="https://fonts.googleapis.com/css2?family=Michroma&family=Raleway:wght@300;400&family=Open+Sans:wght@400&display=swap">
<style>
  :root {
    --stage: #232323;
    --brand-blue: #1d5785;
    --brand-blue-deep: #184b74;
    --paper: #ffffff;
    --ink-blue: #1d5785;
    --ink-grey: #8a8a8a;
  }
  * { box-sizing: border-box; margin: 0; padding: 0; }
  html, body {
    width: 1200px; height: 900px; overflow: hidden;
    background: var(--stage);
  }
  .stage {
    position: relative; width: 1200px; height: 900px;
    display: flex; flex-direction: column; align-items: center; justify-content: center; gap: 40px;
  }
  .card {
    position: relative; width: 660px; height: 390px; overflow: hidden;
    box-shadow: 0 10px 30px rgba(0,0,0,.5);
  }
  /* Back side */
  .card-back { background: var(--brand-blue); }
  .card-back .pattern {
    position: absolute; inset: 0;
    background: linear-gradient(135deg, #1f5b8a 0%, var(--brand-blue) 50%, var(--brand-blue-deep) 100%);
  }
  .brand {
    position: absolute; display: flex; align-items: center; gap: 14px;
    font-family: "Michroma", sans-serif; font-weight: 400; color: var(--paper);
    letter-spacing: 2px;
  }
  .brand-dot {
    width: 34px; height: 34px; border-radius: 50%; background: var(--paper);
  }
  .card-back .brand { left: 60px; bottom: 70px; font-size: 40px; }

  /* Front side */
  .card-front { background: var(--paper); }
  .band {
    position: absolute; left: 0; top: 0; width: 100%; height: 150px;
    background: var(--brand-blue);
  }
  .card-front .brand { left: 40px; top: 40px; font-size: 38px; }
  .person { position: absolute; left: 40px; top: 178px; }
  .person-name {
    font-family: "Michroma", sans-serif; font-size: 22px; color: var(--ink-blue);
    letter-spacing: 1px; text-transform: uppercase;
  }
  .person-role {
    font-family: "Raleway", sans-serif; font-weight: 300; font-size: 17px; color: var(--ink-grey);
    margin-top: 2px;
  }
  .phones { position: absolute; left: 40px; top: 250px; list-style: none; }
  .phones li {
    display: flex; align-items: center; gap: 10px;
    font-family: "Raleway", sans-serif; font-weight: 300; font-size: 19px; color: var(--ink-grey);
    line-height: 26px;
  }
  .phones svg { width: 16px; height: 18px; fill: var(--ink-blue); }
  .address {
    position: absolute; left: 40px; top: 318px; font-style: normal;
    font-family: "Raleway", sans-serif; font-weight: 300; font-size: 16px; color: var(--ink-grey);
    line-height: 20px;
  }
  .web {
    position: absolute; right: 30px; bottom: 22px; list-style: none; text-align: right;
  }
  .web li {
    display: flex; align-items: center; justify-content: flex-end; gap: 10px;
    font-family: "Open Sans", sans-serif; font-size: 18px; color: var(--ink-grey); line-height: 28px;
  }
  .web svg { width: 20px; height: 18px; fill: var(--ink-blue); }
</style>
</head>
<body>
<main class="stage">
  <section class="card card-back" aria-label="Business card back">
    <div class="pattern" role="img" aria-label="Tonal blue background pattern of repeating brand symbols"></div>
    <div class="brand"><span class="brand-dot"></span><span class="brand-name">QUORVEX</span></div>
  </section>

  <section class="card card-front" aria-label="Business card front">
    <div class="band"></div>
    <div class="brand"><span class="brand-dot"></span><span class="brand-name">QUORVEX</span></div>

    <div class="person">
      <h1 class="person-name">Lena Holmqvist</h1>
      <p class="person-role">Chief Financial Officer (CFO)</p>
    </div>

    <ul class="phones">
      <li>
        <svg viewBox="0 0 24 24" aria-hidden="true"><path d="M6.6 10.8a15.1 15.1 0 0 0 6.6 6.6l2.2-2.2a1 1 0 0 1 1-.25 11.4 11.4 0 0 0 3.6.57 1 1 0 0 1 1 1V20a1 1 0 0 1-1 1A17 17 0 0 1 3 4a1 1 0 0 1 1-1h3.5a1 1 0 0 1 1 1c0 1.25.2 2.45.57 3.57a1 1 0 0 1-.25 1z"/></svg>
        +46 8 61 94 27
      </li>
      <li>
        <svg viewBox="0 0 24 24" aria-hidden="true"><path d="M7 1h10a2 2 0 0 1 2 2v18a2 2 0 0 1-2 2H7a2 2 0 0 1-2-2V3a2 2 0 0 1 2-2zm0 3v14h10V4zm5 15.5a1 1 0 1 0 0 2 1 1 0 0 0 0-2z"/></svg>
        +46735 21 47 83
      </li>
    </ul>

    <address class="address">
      Quorvex Sweden AB<br>
      Bruksvägen 14, SE-175 43 JÄRFÄLLA<br>
      Sweden
    </address>

    <ul class="web">
      <li>info@quorvex-example.com
        <svg viewBox="0 0 24 20" aria-hidden="true"><path d="M1 2h22v16H1zm2 2v.4l9 6.2 9-6.2V4zm0 2.8V16h18V6.8l-9 6.2z"/></svg>
      </li>
      <li>www.quorvex-example.com
        <svg viewBox="0 0 24 24" aria-hidden="true"><path d="M12 1a11 11 0 1 0 0 22 11 11 0 0 0 0-22zm7.9 10h-3.4a17 17 0 0 0-1.4-6.6A9 9 0 0 1 19.9 11zM12 3.1c.9 1.3 2.3 4 2.5 7.9h-5C9.7 7.1 11.1 4.4 12 3.1zM8.9 4.4A17 17 0 0 0 7.5 11H4.1a9 9 0 0 1 4.8-6.6zM4.1 13h3.4a17 17 0 0 0 1.4 6.6A9 9 0 0 1 4.1 13zm7.9 7.9c-.9-1.3-2.3-4-2.5-7.9h5c-.2 3.9-1.6 6.6-2.5 7.9zm3.1-1.3a17 17 0 0 0 1.4-6.6h3.4a9 9 0 0 1-4.8 6.6z"/></svg>
      </li>
    </ul>
  </section>
</main>
</body>
</html>
```